Brelto Kemp Flyer Insert

Hi my name is Dorian 

I’ve started a small company supplying hair brushes i need a small flyer made (most like will be A3 size or A4) that i aim to put in the packaging with my products … ive had a look at your portfolio and im a big fan of your work and feel you’d be the perfect designer to create what im looking for. the flyer needs to be a simple manual on how to achieve a hair pattern called 360 waves using my product. Ive had artwork created to go with the flyer and ive written instructions to go with each process of the art work. 

in terms of colour schemes i would like a cool modern black colour scheme theme … weather that is black and white or black and grey or black white and a variety of greys. i trust in your creativity to pull something really cool and professional off. let me know if this is something you be willing to work on and we can get straight down to the payments.

How To Properly Achieve 360 Waves 1. The most time efficient way to achieve waves  covering your entire head , is to start with a low and evenly cut hair cut.  2. Brush  your hair in a direction that your hair naturally grows ….  If you are unsure, brush where your hair best flattens and creates a swirl …from the swirl, brush outward towards the edge of your hair.  TIP: Brush your hair using long straight strokes as keeping a straight stroke creates a more uniform wave pattern. 3. Brush each section multiple times. The more consistent you brush , the more trained and uniform your waves become.  Fact: The Brelto Kemp Wave Brush is designed to cover more head space while brushing so it does not take as long as other regular brushes to achieve waves  Tip: Use a good pomade to help lock in your wave pattern progress in place.  Tip: Let the brush bristles do the work. DO NOT  press too hard, but allow brush bristles to gently pull and snap the hair into place using long straight strokes. 4. Tie hair down using a Durag or a stocking cap. Wear over night for best results.     REPEAT STEPS 1-4 Giving Your Self 3-4 Weeks Between Fresh Cuts  5  After Consistent Brushing , 360 Waves Should Be Complete After Several Months But Will Be Visible After A Couple Of Weeks … Remember Patients And consistency is key and #KEEPUPTHECOMBING #BreltoKemp

Requirements
Must have
• How To Properly Achieve 360 Waves
• 1.
• The most time efficient way to achieve waves  covering your entire head , is to start with a low and evenly cut hair cut. 
• 2.
• Brush  your hair in a direction that your hair naturally grows ….  If you are unsure, brush where your hair best flattens and creates a swirl …from the swirl, brush outward towards the edge of your hair. 
• TIP: Brush your hair using long straight strokes as keeping a straight stroke creates a more uniform wave pattern.
• 3. Brush each section multiple times. The more consistent you brush , the more trained and uniform your waves become. 
• Fact: The Brelto Kemp Wave Brush is designed to cover more head space while brushing so it does not take as long as other regular brushes to achieve waves 
• Tip: Use a good pomade to help lock in your wave pattern progress in place. 
• Tip: Let the brush bristles do the work. DO NOT  press too hard, but allow brush bristles to gently pull and snap the hair into place using long straight strokes.
• 4.
• Tie hair down using a Durag or a stocking cap. Wear over night for best results. 
•   
• REPEAT STEPS 1-4 Giving Your Self 3-4 Weeks Between Fresh Cuts 
• After Consistent Brushing , 360 Waves Should Be Complete After Several Months But Will Be Visible After A Couple Of Weeks … Remember Patients And consistency is key and #KEEPUPTHECOMBING #BreltoKemp

```html
<!DOCTYPE html>
<html lang="en">
<head>
<meta charset="utf-8">
<title>Brelto Kemp – How To Properly Achieve 360 Waves</title>
<link rel="stylesheet" href="https://fonts.googleapis.com/css2?family=Oswald:wght@600&family=Montserrat:wght@600;800;900&family=Source+Sans+3:wght@400;700&family=PT+Sans+Narrow:wght@400;700&display=swap">
<style>
  :root {
    --page: #ffffff;
    --flyer: #181818;
    --ink: #ffffff;
    --text: #2a2a2a;
    --bar-light: #ececec;
    --bar-dark: #c9c9c9;
    --badge: #555555;
    --badge-ring: #2c2c2c;
    --art-a: #5a4a3f;
    --art-b: #6f7a70;
  }
  * { box-sizing: border-box; margin: 0; padding: 0; }
  html, body { width: 1200px; height: 1200px; overflow: hidden; background: var(--page); }
  .flyer {
    position: absolute; left: 234px; top: 84px;
    width: 912px; height: 1290px;
    background: var(--flyer);
    transform: scale(0.8); transform-origin: 0 0;
    font-family: "Source Sans 3", sans-serif;
    color: var(--text);
    box-shadow: 14px 14px 18px rgba(0,0,0,0.35);
  }
  .brand { position: absolute; left: 62px; top: 80px; width: 200px; text-align: center; color: var(--ink); }
  .brand-mark { width: 130px; height: 130px; border-radius: 50%; background: var(--ink); margin: 0 auto 40px; }
  .brand-name { font-family: "Montserrat", sans-serif; font-weight: 600; font-size: 30px; letter-spacing: 2px; line-height: 1.1; }
  .title { position: absolute; left: 317px; top: 0; width: 560px; color: var(--ink); line-height: 1; font-weight: normal; }
  .title span { position: absolute; left: 0; white-space: nowrap; transform-origin: 0 0; }
  .title-top { top: 58px; font-family: "Oswald", sans-serif; font-weight: 600; font-size: 86px; letter-spacing: -2px; transform: scaleX(0.9); }
  .title-mid { top: 140px; font-family: "Montserrat", sans-serif; font-weight: 800; font-size: 84px; transform: scaleX(1.2); }
  .title-low { top: 222px; font-family: "Montserrat", sans-serif; font-weight: 900; font-size: 84px; letter-spacing: -1px; }
  .bar {
    position: absolute; border-radius: 22px;
    background: linear-gradient(180deg, var(--bar-light) 55%, var(--bar-dark));
    font-size: 15px; line-height: 20px;
  }
  .note { font-family: "PT Sans Narrow", sans-serif; font-size: 13.5px; line-height: 20px; letter-spacing: -0.1px; }
  .note b { font-size: 16px; }
  .badge {
    position: absolute; width: 72px; height: 72px; border-radius: 50%;
    background: var(--badge); border: 4px solid var(--badge-ring);
    color: var(--ink); font-family: "Montserrat", sans-serif; font-weight: 900; font-size: 44px;
    display: flex; align-items: center; justify-content: center;
  }
  .art {
    position: absolute; width: 130px; height: 130px; border-radius: 50%;
    border: 3px solid var(--ink);
    background: radial-gradient(circle at 55% 40%, var(--art-a) 0 35%, var(--art-b) 70%, #f2f2f2 71%);
  }
  .repeat { position: absolute; left: 0; width: 912px; top: 1008px; text-align: center; color: var(--ink); font-size: 18px; }
  .tags { display: block; text-align: center; font-size: 15px; margin-top: 4px; padding-left: 40px; }
  .url { position: absolute; left: 0; width: 912px; top: 1222px; text-align: center; color: var(--ink); font-family: "Montserrat", sans-serif; font-weight: 600; font-size: 20px; letter-spacing: 4px; }
</style>
</head>
<body>
<main class="flyer">
  <header>
    <div class="brand">
      <div class="brand-mark"></div>
      <div class="brand-name">BRELTO<br>KEMP</div>
    </div>
    <h1 class="title">
      <span class="title-top">HOW TO PROPERLY</span>
      <span class="title-mid">ACHIEVE</span>
      <span class="title-low">360 WAVES</span>
    </h1>
  </header>

  <section class="step step-1">
    <div class="bar" style="left:120px;top:393px;width:677px;height:77px;padding:18px 80px 0 49px;">
      <p>The most time efficient way to achieve waves &nbsp;covering your entire head , is to start with a low and evenly cut hair cut.</p>
    </div>
    <div class="badge" style="left:76px;top:361px;">1</div>
    <div class="art" style="left:735px;top:340px;" role="img" aria-label="Illustration of a man in profile with a fresh low haircut"></div>
  </section>

  <section class="step step-2">
    <div class="bar" style="left:107px;top:518px;width:695px;height:130px;padding:16px 24px 0 91px;">
      <p style="max-width:530px;text-align:justify;">Brush &nbsp;your hair in a direction that your hair naturally grows If you are unsure, brush where your hair best flattens and creates a swirl from the swirl, brush outward towards the edge of your hair.</p>
      <p class="note" style="margin-top:12px;white-space:nowrap;"><b>TIP:</b> Brush your hair using long straight strokes as keeping a straight stroke creates a more uniform wave pattern.</p>
    </div>
    <div class="art" style="left:49px;top:520px;" role="img" aria-label="Illustration of a man brushing the side of his hair"></div>
    <div class="badge" style="left:763px;top:504px;">2</div>
  </section>

  <section class="step step-3">
    <div class="bar" style="left:112px;top:685px;width:690px;height:172px;padding:10px 78px 0 47px;">
      <p style="text-align:justify;">Brush each section multiple times. The more consistent you brush , the more trained and uniform your waves become.</p>
      <p class="note" style="margin-top:6px;"><b>Fact:</b> The Brelto Kemp Wave Brush is designed to cover more head space while brushing so it does not take as long as other regular brushes to achieve waves</p>
      <p class="note" style="margin-top:3px;"><b>Tip:</b> Use a good pomade to help lock in your wave pattern progress in place.</p>
      <p class="note" style="margin-top:3px;"><b>Tip:</b> Let the brush bristles do the work. DO NOT &nbsp;press too hard, but allow brush bristles to gently pull and snap the hair into place using long straight strokes.</p>
    </div>
    <div class="badge" style="left:77px;top:674px;">3</div>
    <div class="art" style="left:735px;top:695px;" role="img" aria-label="Illustration of a man brushing the top of his hair with a wave brush"></div>
  </section>

  <section class="step step-4">
    <div class="bar" style="left:150px;top:915px;width:652px;height:65px;padding:22px 40px 0 48px;">
      <p style="white-space:nowrap;">Tie hair down using a Durag or a stocking cap. Wear over night for best results.</p>
    </div>
    <div class="art" style="left:47px;top:875px;" role="img" aria-label="Illustration of a man wearing a durag"></div>
    <div class="badge" style="left:763px;top:910px;">4</div>
  </section>

  <p class="repeat"><b>REPEAT STEPS</b> 1-4 Giving Your Self 3-4 Weeks Between Fresh Cuts</p>

  <section class="step step-5">
    <div class="bar" style="left:112px;top:1052px;width:690px;height:116px;padding:22px 135px 0 47px;">
      <p>After Consistent Brushing , 360 Waves Should Be Complete After Several Months But Will Be Visible After A Couple Of Weeks &nbsp;Remember Patients And consistency is key and
        <span class="tags"><b>#KEEPUPTHECOMBING</b> #BreltoKemp</span></p>
    </div>
    <div class="badge" style="left:77px;top:1031px;">5</div>
    <div class="art" style="left:735px;top:1045px;" role="img" aria-label="Illustration of a man showing finished 360 waves"></div>
  </section>

  <footer class="url">www.BreltoKempBrush</footer>
</main>
</body>
</html>
```